CV brochure for Top Management Position

I need me to introduce myself a brochure design for a CV brochure in. So sort of a resume in booklet format. The design should be serious for a convey on the other, the viewer that I stand for the new world of digitization. The brochure is intended to convey that I am a "Digital Leader". With the brochure boards, boards of directors and decision makers of enterprises should pay attention to my person. It must not be a 0815 design of the rod. The design should already be addressed with the front page of the topic Digital Leader, since the front page usually is the decisive criterion whether to continue dealing with the person or not. I am now CIO (IT manager) and wants to move with the brochure myself from this technique corner out and thus make it interesting for other positions. The positions are in absolute top management, the board, management, supervisory anchored and deal primarily with the digital transformation and the new digital world. So should appear with security on the front page a concise picture of me. but I am also very open to any alternative proposal brochure. Here you can see my current CV with picture and the basic content. The brochure is even more responsive to the social skills and not only to the technical projects implemented as before.

Target Market(s)

Top management, CxO level, supervisory boards, large companies, large Mittlestandsunternehmen

Industry/Entity Type

Management

Font styles to use
Serif
Sans Serif

Requirements
Must have
• see description
Nice to have
• see description
Should not have
• see description

```html
<!DOCTYPE html>
<html lang="de">
<head>
<meta charset="utf-8">
<title>Curriculum Vitae – Dr. Markus Brenner</title>
<link rel="stylesheet" href="https://fonts.googleapis.com/css2?family=Encode+Sans:wght@300;400&family=Encode+Sans+Condensed:ital,wght@0,300;0,400&family=Encode+Sans+Expanded:wght@800&display=swap">
<style>
  :root {
    --navy: #1f3360;
    --navy-deep: #16264d;
    --orange: #f26a1f;
    --white: #ffffff;
    --tag-grey: #e6e6e6;
    --text-dark: #1f2f55;
    --blue-mid: #4f74b8;
    --blue-light: #c2d0ea;
  }
  * { margin: 0; padding: 0; box-sizing: border-box; }
  html, body { width: 849px; height: 1200px; overflow: hidden; background: var(--white); }
  .cover {
    position: relative; width: 849px; height: 1200px; overflow: hidden;
    font-family: "Encode Sans Condensed", "Arial Narrow", sans-serif;
    font-weight: 300; color: var(--text-dark);
  }
  .backdrop {
    position: absolute; inset: 0;
    background:
      linear-gradient(180deg, rgba(255,255,255,0) 0%, rgba(255,255,255,0) 88%, rgba(22,38,77,0.55) 100%),
      linear-gradient(160deg, #ffffff 0%, #ffffff 30%, #e3e9f5 42%, #a9bde2 55%, #5d7fc0 70%, #3f63a8 82%, #2a4a8e 100%);
  }
  .fade-top {
    position: absolute; left: 0; top: 0; width: 849px; height: 560px;
    background: radial-gradient(ellipse at 60% 30%, #ffffff 55%, rgba(255,255,255,0) 100%);
  }
  .contact-band {
    position: absolute; left: 0; top: 918px; width: 508px; height: 210px;
    background: rgba(208,220,242,0.55);
  }
  .bottom-band {
    position: absolute; left: 0; top: 1128px; width: 849px; height: 72px;
    background: linear-gradient(90deg, #1d3668 0%, #3a63b0 45%, #2f55a0 70%, #6a8bc8 100%);
  }
  .side-column {
    position: absolute; left: 508px; top: 0; width: 236px; height: 1200px;
    background: var(--navy);
  }
  .side-title {
    position: absolute; left: 744px; top: 0; width: 105px; height: 1200px;
    background: var(--white);
  }
  .side-title svg { position: absolute; left: 0; top: 0; }
  .section-heading {
    position: absolute; left: 450px; top: 30px;
    font-family: "Encode Sans", sans-serif; font-weight: 300; font-size: 39px;
    color: var(--navy); white-space: nowrap; letter-spacing: -0.5px;
  }
  .section-heading .on-dark { color: var(--white); }
  .accent { color: var(--orange); }
  .doc-title {
    position: absolute; right: 383px; top: 186px;
    font-family: "Encode Sans", sans-serif; font-weight: 300; font-size: 47px;
    color: var(--navy); white-space: nowrap; letter-spacing: -0.5px;
  }
  .side-text {
    position: absolute; left: 516px; width: 226px;
    font-size: 16.5px; line-height: 22.4px; color: var(--white);
  }
  .side-text em { font-style: italic; }
  .side-text.bullet { left: 521px; }
  .side-text.bullet::before {
    content: ""; position: absolute; left: -13px; top: 5px;
    border-left: 8px solid var(--orange);
    border-top: 6px solid transparent; border-bottom: 6px solid transparent;
  }
  .portrait {
    position: absolute; left: 477px; top: 252px; width: 294px; height: 294px;
    border-radius: 50%; border: 4px solid var(--white);
    background: radial-gradient(circle at 50% 40%, #e2b9a2 0%, #cfa08a 26%, #c9c9c9 46%, #d9d9d9 70%, #2a2a2e 100%);
  }
  .trait {
    position: absolute; height: 17px; background: var(--tag-grey);
    font-size: 16.5px; line-height: 17px; color: var(--text-dark);
    text-align: right; padding-right: 34px;
  }
  .trait::after {
    content: ""; position: absolute; right: 14px; top: -2px;
    border-right: 10px solid var(--orange);
    border-top: 10px solid transparent; border-bottom: 10px solid transparent;
  }
  .name {
    position: absolute; right: 381px; top: 552px;
    font-family: "Encode Sans", sans-serif; font-weight: 300; font-size: 50px;
    color: var(--navy); white-space: nowrap; letter-spacing: -0.5px;
  }
  .role {
    position: absolute; right: 381px; top: 610px;
    font-size: 16.5px; color: var(--navy); white-space: nowrap;
  }
  .role .divider { color: var(--orange); }
  .contact-divider {
    position: absolute; left: 220px; top: 920px; width: 2px; height: 208px;
    background: var(--orange);
  }
  .contact-label, .contact-value {
    position: absolute; font-size: 16.5px; line-height: 28.3px; color: var(--text-dark);
  }
  .contact-label { right: 649px; text-align: right; top: 925px; }
  .contact-value { left: 241px; top: 925px; }
</style>
</head>
<body>
<main class="cover">
  <div class="backdrop"></div>
  <div class="fade-top"></div>
  <div class="contact-band"></div>
  <div class="bottom-band"></div>

  <aside class="side-column"></aside>
  <div class="side-title">
    <svg width="105" height="1200" viewBox="0 0 105 1200" aria-label="Wirtschaftsinformatik">
      <text transform="translate(748 2) rotate(90)" x="0" y="0" dy="-8" fill="#f26a1f"
            font-family="'Encode Sans Expanded', sans-serif" font-weight="800" font-size="50"
            textLength="1196" lengthAdjust="spacing" transform-origin="0 0"
            style="transform: translate(-744px, 0) translate(747px, 2px) rotate(90deg);">WIRTSCHAFTSINFORMATIK</text>
    </svg>
  </div>

  <h2 class="section-heading">Auf <span class="on-dark">einen </span><span class="accent">B</span><span class="on-dark">lick</span></h2>

  <p class="side-text" style="top:79px;">
    <em>Kommunikationsstarke<br>Führungspersönlichkeit</em> mit<br>mehrjähriger Erfahrung in<br>Leitungsfunktionen im<br><em>IT-Bereich</em>, aktuell<br><em>Chief Information Officer</em> (CIO)<br>und <em>Chief Digital Officer</em> (CDO)
  </p>

  <h1 class="doc-title"><span class="accent">C</span>urriculum <span class="accent">V</span>itae</h1>

  <div class="trait" style="left:316px; top:332px; width:172px;">umsetzungsstark</div>
  <div class="trait" style="left:301px; top:376px; width:175px;">lösungsorientiert</div>
  <div class="trait" style="left:300px; top:420px; width:176px;">unternehmerisch</div>
  <div class="trait" style="left:313px; top:464px; width:179px;">visionär</div>

  <div class="portrait" role="img" aria-label="Porträtfoto von Dr. Markus Brenner"></div>

  <h2 class="name">Dr. <span class="accent">M</span>arkus <span class="accent">B</span>renner</h2>
  <p class="role">Chief Information Officer (CIO) <span class="divider">|</span> Ph.D.</p>

  <p class="side-text" style="top:555px;">Umfangreiche<br>Fachexpertise in:</p>
  <p class="side-text bullet" style="top:604px;">Konzeption und<br>Weiterentwicklung von<br>IT-Unternehmensstrategien</p>
  <p class="side-text bullet" style="top:674px;">Effizienzsteigerung<br>im IT-Bereich</p>
  <p class="side-text bullet" style="top:723px;">Optimierung der<br>IT-Service-Strukturen</p>
  <p class="side-text bullet" style="top:772px;">Planung und Durchführung<br>konzernweiter IT-Programme</p>
  <p class="side-text" style="top:821px;">Experte auf dem Gebiet der<br><em>Transformation von<br>Unternehmen in die<br>digitale Welt</em> (Industrie 4.0)</p>
  <p class="side-text" style="top:917px;">Etablierung der IT<br>als Business Enabler</p>
  <p class="side-text" style="top:967px;">Führung von 75 MA + ca. 20<br>(weltweite und externe),<br>davon 4 Führungskräfte<br>Budget i.H.v. 22 Mio. € p.a.</p>
  <p class="side-text" style="top:1063px;"><em>Wissensmanager</em> mit <em>inter-<br>kultureller Kompetenz</em>, breitem<br>Technologieverständnis sowie<br>ausgeprägter Durchsetzungs-<br>und Teamfähigkeit</p>

  <div class="contact-divider"></div>
  <p class="contact-label">Adresse<br><br>Geburtsdaten<br>Familienstand<br>Mobil<br>E-Mail<br>Profil</p>
  <p class="contact-value">Lindenweg 14<br>10115 Berlin<br>12. Mai 1978 in Konstanz<br>verheiratet | 2 Kinder<br>+ 49 (0) 170 55 0123 45<br>kontakt@brenner-mail.de<br>https://www.netzprofil.de/brenner/</p>
</main>
</body>
</html>
```